Flier redesign

Sample fliers are attached from previous 2 years "Seasonal care 2018" and "2019 Seasonal Care" . Need an updated design for this year.

Possible images are attached to this brief. If you use the before/after pictures - you should use both of them. Use images attached to this brief or any from our website that you may prefer.

Colors

Designer to choose colors to be used in the design.

Requirements
Must have
• Colors should match our website theme. www.hollowbrookgardens.org
• Should be a "new" design, not just copying one of the prior year designs with a different image.
• Must be created in photoshop and file must be provided at the end.
• Text should be the same as 2019 version.

```html
<!DOCTYPE html>
<html lang="en">
<head>
<meta charset="utf-8">
<title>Hollowbrook Gardens – Care Plans</title>
<link rel="stylesheet" href="https://fonts.googleapis.com/css2?family=Bebas+Neue&family=Dosis:wght@400;500;700&family=Merriweather+Sans:wght@300;400&display=swap">
<style>
  :root{
    --maroon:#7a1f2e;
    --maroon-dark:#6a1826;
    --white:#ffffff;
    --text:#5a5a5a;
    --text-dark:#444444;
    --tick:#35b24a;
    --badge:#f4c542;
    --leaf-light:#8fbf55;
    --leaf-dark:#3f6b2a;
  }
  *{box-sizing:border-box;margin:0;padding:0}
  html,body{width:1200px;height:1200px;overflow:hidden;background:var(--white)}
  .canvas{position:relative;width:1200px;height:1200px;background:var(--white)}
  .backdrop{position:absolute;left:133px;top:0;width:934px;height:1200px}
  .brand{position:absolute;left:456px;top:0;width:280px;height:86px;background:var(--white);
    border-radius:0 0 60px 60px;display:flex;align-items:center;justify-content:center;gap:10px}
  .brand-dot{width:14px;height:14px;border-radius:50%;background:var(--maroon)}
  .brand-name{font-family:"Dosis",sans-serif;font-weight:500;font-size:22px;color:var(--maroon);letter-spacing:1px;text-transform:uppercase}
  .plan-head{position:absolute;background:var(--maroon);color:var(--white);text-align:center;
    font-family:"Dosis",sans-serif;display:flex;flex-direction:column;align-items:center;justify-content:center;
    clip-path:polygon(0 4%,2% 0,98% 0,100% 4%,100% 86%,50% 100%,0 86%);padding-bottom:14px}
  .plan-title{font-weight:700;font-size:26px;line-height:1.25;letter-spacing:.5px}
  .plan-sub{font-weight:400;font-size:18px;line-height:1.35;margin-top:12px}
  .plan-body{position:absolute;background:var(--white);border-radius:0 0 14px 14px;
    box-shadow:0 4px 10px rgba(0,0,0,.12);font-family:"Merriweather Sans",sans-serif;color:var(--text)}
  .features{list-style:none}
  .features li{position:relative;padding-left:19px;font-weight:300;font-size:10.5px;line-height:1.4;margin-bottom:10px}
  .features li svg{position:absolute;left:0;top:2px;width:12px;height:10px}
  .features.large li{font-size:12.5px}
  .price-label{font-family:"Dosis",sans-serif;font-size:14px;text-align:center;letter-spacing:.5px;line-height:1.3;color:var(--text)}
  .price{font-family:"Dosis",sans-serif;font-weight:700;font-size:22px;text-align:center;color:var(--text-dark);margin-top:6px}
  .terms{display:flex;justify-content:space-between;margin-top:22px}
  .term{flex:1;text-align:center;font-family:"Dosis",sans-serif}
  .term + .term{border-left:1px solid #eee}
  .term-len{font-size:13px;color:var(--text)}
  .term-price{font-weight:700;font-size:17px;color:var(--text-dark);margin-top:4px}
  .badge{position:absolute;left:924px;top:842px;width:96px;height:64px;background:var(--badge);
    transform:rotate(-10deg);border-radius:3px;box-shadow:0 2px 4px rgba(0,0,0,.2);
    font-family:"Dosis",sans-serif;text-align:center;color:#222;font-weight:700;line-height:1}
  .badge-main{font-size:25px;margin-top:8px}
  .badge-sub{font-size:14px;margin-top:1px}
  .badge-string{position:absolute;left:930px;top:823px}
  .footer{position:absolute;left:133px;top:1124px;width:934px;height:76px;background:var(--maroon);
    color:var(--white);font-family:"Bebas Neue",sans-serif;display:flex;align-items:center;justify-content:space-between;padding:0 30px}
  .footer-link{font-size:29px;letter-spacing:.3px}
  .footer-call{text-align:center;line-height:.95}
  .footer-call span{display:block;font-size:38px}
</style>
</head>
<body>
<div class="canvas">
  <svg class="backdrop" viewBox="0 0 934 1200" width="934" height="1200" aria-hidden="false">
    <defs>
      <linearGradient id="foliage" x1="0" y1="0" x2="0" y2="1">
        <stop offset="0" stop-color="#6e9e3e"/>
        <stop offset=".5" stop-color="var(--leaf-dark)"/>
        <stop offset="1" stop-color="var(--leaf-light)"/>
      </linearGradient>
    </defs>
    <rect x="0" y="0" width="934" height="700" fill="url(#foliage)" role="img" aria-label="Photo of tree-lined cemetery lawn with rows of headstones"/>
    <path d="M0 632 Q467 480 934 608 L934 1200 L0 1200 Z" fill="var(--maroon)"/>
    <path d="M0 684 Q467 528 934 680 L934 1200 L0 1200 Z" fill="var(--white)"/>
  </svg>

  <div class="brand">
    <span class="brand-dot"></span>
    <span class="brand-name">Hollowbrook Gardens</span>
  </div>

  <!-- Seasonal -->
  <div class="plan-head" style="left:198px;top:532px;width:219px;height:180px">
    <div class="plan-title">SEASONAL CARE</div>
    <div class="plan-sub">Seasonal landscaping<br>grave care</div>
  </div>
  <div class="plan-body" style="left:205px;top:706px;width:210px;height:246px;padding:28px 6px 0 3px">
    <ul class="features large">
      <li><svg viewBox="0 0 12 10"><path d="M1 5l3.5 3.5L11 1" stroke="var(--tick)" stroke-width="1.6" fill="none"/></svg>Weeding and trimming services on your gravesite approximately every 7 weeks during the growing season: mid-April through mid-October</li>
    </ul>
    <div class="terms">
      <div class="term"><div class="term-len">1YEAR</div><div class="term-price">115$</div></div>
      <div class="term"><div class="term-len">2YEARS</div><div class="term-price">230$</div></div>
      <div class="term"><div class="term-len">3YEARS</div><div class="term-price">345$</div></div>
    </div>
  </div>

  <!-- Basic -->
  <div class="plan-head" style="left:489px;top:480px;width:220px;height:180px">
    <div class="plan-title">BASIC CARE<br>ENDOWMENT</div>
    <div class="plan-sub" style="margin-top:8px">Landscaping care forever<br>for graves with no plantings</div>
  </div>
  <div class="plan-body" style="left:494px;top:652px;width:210px;height:248px;padding:18px 6px 0 8px">
    <ul class="features">
      <li><svg viewBox="0 0 12 10"><path d="M1 5l3.5 3.5L11 1" stroke="var(--tick)" stroke-width="1.6" fill="none"/></svg>Weeding and trimming services on your gravesite 2 times per year mid-May and mid-September.</li>
      <li><svg viewBox="0 0 12 10"><path d="M1 5l3.5 3.5L11 1" stroke="var(--tick)" stroke-width="1.6" fill="none"/></svg>Monument leveling</li>
      <li><svg viewBox="0 0 12 10"><path d="M1 5l3.5 3.5L11 1" stroke="var(--tick)" stroke-width="1.6" fill="none"/></svg>Payment ensures grave care forever</li>
    </ul>
    <div class="price-label" style="margin-top:14px">12 MONTHLY<br>PAYMENTS OF</div>
    <div class="price">239$</div>
  </div>

  <!-- Perpetual -->
  <div class="plan-head" style="left:771px;top:373px;width:219px;height:179px">
    <div class="plan-title">PERPETUAL CARE<br>ENDOWMENT</div>
    <div class="plan-sub" style="margin-top:8px">Landscaping care forever<br>for graves with plantings.</div>
  </div>
  <div class="plan-body" style="left:776px;top:540px;width:210px;height:300px;padding:20px 4px 0 4px">
    <ul class="features">
      <li style="margin-bottom:6px"><svg viewBox="0 0 12 10"><path d="M1 5l3.5 3.5L11 1" stroke="var(--tick)" stroke-width="1.6" fill="none"/></svg>Weeding and filming services on your gravesite approximately every 7 weeks during the growing season: mid-April through mid-October</li>
      <li style="margin-bottom:6px"><svg viewBox="0 0 12 10"><path d="M1 5l3.5 3.5L11 1" stroke="var(--tick)" stroke-width="1.6" fill="none"/></svg>Monument leveling and cleaning</li>
      <li style="margin-bottom:6px"><svg viewBox="0 0 12 10"><path d="M1 5l3.5 3.5L11 1" stroke="var(--tick)" stroke-width="1.6" fill="none"/></svg>Payment ensures grave care forever</li>
      <li style="margin-bottom:6px"><svg viewBox="0 0 12 10"><path d="M1 5l3.5 3.5L11 1" stroke="var(--tick)" stroke-width="1.6" fill="none"/></svg>Full bed of boxwood shrubs</li>
      <li style="margin-bottom:6px"><svg viewBox="0 0 12 10"><path d="M1 5l3.5 3.5L11 1" stroke="var(--tick)" stroke-width="1.6" fill="none"/></svg>Replacement of shrubs</li>
      <li style="margin-bottom:6px"><svg viewBox="0 0 12 10"><path d="M1 5l3.5 3.5L11 1" stroke="var(--tick)" stroke-width="1.6" fill="none"/></svg>Trust certificate</li>
    </ul>
    <div class="price-label" style="margin-top:10px">12 MONTHLY<br>PAYMENTS OF</div>
    <div class="price">297$</div>
  </div>

  <svg class="badge-string" width="80" height="40" viewBox="0 0 80 40">
    <path d="M8 30 L38 6 L70 24" stroke="#333" stroke-width="1.5" fill="none"/>
    <circle cx="38" cy="6" r="4" fill="#888"/>
  </svg>
  <div class="badge">
    <div class="badge-main">MOST</div>
    <div class="badge-sub">POPULAR</div>
  </div>

  <footer class="footer">
    <span class="footer-link">WWW.HOLLOWBROOKGARDENS.ORG</span>
    <div class="footer-call"><span>CALL US</span><span>(201) 555-0148</span></div>
    <span class="footer-link">INFO@HOLLOWBROOKGARDENS.ORG</span>
  </footer>
</div>
</body>
</html>
```